Flyer Handout when attending Dental Conventions, or dental office shows

take the sample file folder that is shown with 2 pictures. The outside and inside of the folder needs to be completed, along with the inserts. This folder pictures are from someone elses flyer/folder and i would like to have it layout like this. The KPW inserts is informational, but it is lacking originality, pictures, etc. Try to make our information and move it to 2017. When this is done, i would like to take this flyer and load it to the web or allow to send via email and make it interactive. The user can select the flyers and it will slide or flip to the flyer. this will make if kewl/fun

Target Market(s)

Dental Offices

Industry/Entity Type

Dental

Font styles to use
Serif
Sans Serif

Colors

Designer to choose colors to be used in the design.

Requirements
Must have
• a Semi new look and feel of our flyers, and a new envelope created

```html
<!DOCTYPE html>
<html lang="en">
<head>
<meta charset="utf-8">
<title>KPW Real-Time Eligibility – Folder and Insert</title>
<link href="https://fonts.googleapis.com/css2?family=Open+Sans:wght@400;600;700&family=Oswald:wght@400;500&display=swap" rel="stylesheet">
<style>
  :root{
    --stage:#efefef;
    --folder-blue:#2a93c9;
    --folder-blue-dark:#1f78a8;
    --accent-orange:#f39a3c;
    --flyer-blue:#4f88c9;
    --flyer-blue-dark:#2f62a8;
    --ink:#333840;
    --soft-gray:#eceef1;
    --paper:#ffffff;
    --sky-top:#c9dbe8;
    --sky-bottom:#6f8fa6;
  }
  *{box-sizing:border-box;margin:0;padding:0}
  html,body{width:1200px;height:557px;overflow:hidden;background:var(--stage)}
  body{font-family:"Open Sans",Arial,sans-serif;color:var(--ink);position:relative}

  /* ---------- Folder spread ---------- */
  .folder{position:absolute;left:60px;top:68px;width:640px;height:420px;display:flex;box-shadow:0 10px 24px rgba(0,0,0,.18)}
  .folder-back{width:320px;height:420px;background:linear-gradient(160deg,var(--folder-blue) 0%,var(--folder-blue-dark) 100%);position:relative;color:#fff}
  .folder-contact{position:absolute;left:28px;bottom:30px;font-size:8px;line-height:1.6;letter-spacing:.3px}
  .folder-contact .company{font-size:10px;font-weight:600;letter-spacing:1px;margin-bottom:2px}
  .folder-front{width:320px;height:420px;position:relative;background:linear-gradient(180deg,#fafafa 0%,#d9d9d9 100%)}
  .folder-front svg{position:absolute;inset:0}
  .folder-logo{position:absolute;left:40px;top:22px;font-size:22px;font-weight:700;color:var(--folder-blue);letter-spacing:1px}
  .folder-title{position:absolute;right:22px;top:306px;text-align:right;font-size:15px;font-weight:600;line-height:1.2;color:var(--folder-blue)}

  /* ---------- Insert flyer ---------- */
  .flyer{position:absolute;left:846px;top:55px;width:285px;height:404px;background:var(--paper);box-shadow:0 4px 14px rgba(0,0,0,.22);overflow:hidden}
  .flyer-photo{height:106px;background:linear-gradient(180deg,var(--sky-top) 0%,#dfe6ea 55%,var(--sky-bottom) 100%);position:relative}
  .flyer-logo{position:absolute;left:22px;top:16px;font-size:16px;font-weight:700;color:var(--flyer-blue-dark);letter-spacing:.5px}
  .flyer-headline{height:28px;background:var(--flyer-blue);color:#fff;font-size:10px;font-weight:600;display:flex;align-items:center;justify-content:center}
  .intro{padding:10px 18px 0;text-align:center;height:88px}
  .intro h2{font-size:8.5px;font-weight:700;color:var(--flyer-blue-dark);margin-bottom:9px}
  .intro h3{font-size:6px;font-weight:700;margin-bottom:5px}
  .intro p{font-size:4.3px;line-height:1.45}
  .benefits{background:var(--soft-gray);height:96px;padding:7px 16px 0;text-align:center}
  .benefits h2{font-size:7px;font-weight:700;color:var(--flyer-blue-dark);margin-bottom:6px}
  .benefit-row{display:flex;justify-content:center;gap:9px;margin-bottom:6px}
  .benefit{background:var(--flyer-blue);color:#fff;border-radius:2px;width:73px;height:30px;padding-top:4px;font-size:4.4px;line-height:1.4}
  .benefit strong{display:block;font-size:4.6px;font-weight:700;margin-bottom:2px}
  .benefit.narrow{width:52px}
  .benefit.wide{width:82px}
  .steps{background:var(--flyer-blue);height:52px;color:#fff;display:flex;align-items:flex-start;padding:8px 14px 0;gap:6px}
  .step{flex:1;text-align:center}
  .step h4{font-family:"Oswald","Arial Narrow",sans-serif;font-weight:400;font-size:8px;margin-bottom:2px}
  .step p{font-size:4.4px;line-height:1.4}
  .step-arrows{width:30px;height:30px;margin-top:6px}
  .call{height:34px;display:flex;align-items:center;justify-content:center;gap:8px}
  .call p{font-size:5px;text-align:right;line-height:1.4}
  .call strong{font-family:"Oswald","Arial Narrow",sans-serif;font-weight:500;font-size:10px;color:var(--flyer-blue-dark)}
</style>
</head>
<body>

<section class="folder" aria-label="Presentation folder, outside spread">
  <div class="folder-back">
    <div class="folder-contact">
      <div class="company">KEYSTONE PRACTICE WORKS</div>
      <div>218 Alder Lane, Brookfield, MN 55190 | Phone: 555-014-2230</div>
      <div>Fax: 555-014-2231 | www.kpwdental.example</div>
    </div>
  </div>
  <div class="folder-front">
    <svg width="320" height="420" viewBox="0 0 320 420">
      <defs>
        <linearGradient id="bridgePhoto" x1="0" y1="0" x2="0" y2="1">
          <stop offset="0" stop-color="#bcd3e3"/>
          <stop offset=".5" stop-color="#e6eef3"/>
          <stop offset="1" stop-color="#8fa9bb"/>
        </linearGradient>
      </defs>
      <path d="M45 0 H320 V300 C250 300 200 250 230 195 C120 210 60 110 45 0 Z" fill="var(--folder-blue)"/>
      <path d="M45 0 H320 V200 C220 165 200 210 165 220 C90 200 55 100 45 0 Z" fill="var(--accent-orange)"/>
      <path d="M45 0 H320 V170 C230 150 200 195 170 200 C100 180 60 90 45 0 Z" fill="url(#bridgePhoto)" role="img" aria-label="Photo of a suspension bridge rising above fog"/>
    </svg>
    <div class="folder-logo">KPW</div>
    <div class="folder-title">Bridging the Gap between<br>Payers and Providers</div>
  </div>
</section>

<article class="flyer" aria-label="Real-time eligibility insert">
  <div class="flyer-photo" role="img" aria-label="Photo of a red suspension bridge over a foggy bay">
    <div class="flyer-logo">KPW</div>
  </div>
  <div class="flyer-headline">Bridging the Gap between Payers and Providers</div>

  <section class="intro">
    <h2>Introducing KPW Real-Time Eligibility</h2>
    <h3>We are proud to announce a NEW feature.</h3>
    <p>You are now able to process real-time eligibility. This service is an easy-to-use solution providing instant connectivity to leading commercial and government insurers. This service will help you to automate time-consuming business functions while improving patient services. KPW real-time eligibility consolidates access to multiple payers from a single screen with the one source solution, it allows dental offices to receive eligibility and plan benefit information immediately from insurance companies. Most importantly, the eligibility information received is displayed in an understandable, easy to read format that can be printed and shared with your patient.</p>
  </section>

  <section class="benefits">
    <h2>Benefits</h2>
    <div class="benefit-row">
      <div class="benefit"><strong>DECREASE</strong>the amount of phone calls<br>to insurance companies</div>
      <div class="benefit"><strong>IMPROVE</strong>your patient services by knowing at<br>the time of service what is owed</div>
      <div class="benefit"><strong>EXPEDITE</strong>reimbursements</div>
    </div>
    <div class="benefit-row">
      <div class="benefit narrow"><strong>INCREASE</strong>cash flow</div>
      <div class="benefit wide"><strong>IMPROVE</strong>dental claims acceptance rates</div>
    </div>
  </section>

  <section class="steps">
    <div class="step">
      <h4>HOW IT WORKS</h4>
      <p>Within KPW Bridge, select the NEW Eligibility Tab. Hit send and you will begin receiving all of your eligibility responses within the KPW Portal. It is that easy!</p>
    </div>
    <svg class="step-arrows" viewBox="0 0 30 30" aria-hidden="true">
      <path d="M6 5 L15 15 L6 25 M15 5 L24 15 L15 25" fill="none" stroke="#fff" stroke-width="3"/>
    </svg>
    <div class="step">
      <h4>IMPLEMENTATION</h4>
      <p>Please contact KPW support and we will activate your eligibility service within the KPW Bridge and the KPW Portal within minutes.</p>
    </div>
  </section>

  <footer class="call">
    <p>To find out more information or have any<br>questions about this feature answered please</p>
    <strong>CALL (800) 555-0147</strong>
  </footer>
</article>

</body>
</html>
```